The Perfect Business Card for PineHarbor

I am looking for a business card which beautifully incorporates my logo, reflects my business and looks special, elegant and clean.

```html
<!DOCTYPE html>
<html lang="en">
<head>
<meta charset="utf-8">
<title>PineHarbor Business Card</title>
<link rel="stylesheet" href="https://fonts.googleapis.com/css2?family=Marcellus+SC&family=Marcellus&family=Poppins:wght@400&display=swap">
<style>
  :root {
    --page-bg: #e9e6e1;
    --green-deep: #1f3d14;
    --green-mid: #3f6b22;
    --green-soft: #5d7d49;
    --frost: #e6e2db;
    --frost-edge: #cfc9bf;
    --ink-light: #f3f1ea;
    --brand-green: #2f4a17;
  }
  * { margin: 0; padding: 0; box-sizing: border-box; }
  html, body {
    width: 1200px; height: 969px; overflow: hidden;
    background: var(--page-bg);
  }
  .card {
    position: absolute; left: 100px; top: 200px;
    width: 1000px; height: 568px;
    border-radius: 26px; overflow: hidden;
    box-shadow: 0 14px 40px rgba(0,0,0,0.18);
  }
  .card-bg { position: absolute; inset: 0; }
  .contact {
    position: absolute; left: 61px; top: 140px;
    color: var(--ink-light);
    font-family: "Poppins", sans-serif;
  }
  .contact-name {
    font-family: "Marcellus SC", serif;
    font-size: 33px; letter-spacing: 1.5px; line-height: 1;
  }
  .contact-title { font-size: 20px; margin-top: 8px; }
  .contact-address { font-size: 20px; line-height: 28px; margin-top: 30px; }
  .contact-lines { list-style: none; margin-top: 22px; }
  .contact-lines li {
    display: flex; align-items: center;
    font-size: 20px; line-height: 29px;
  }
  .contact-lines svg { width: 18px; height: 18px; margin-right: 14px; fill: var(--ink-light); }
  .brand {
    position: absolute; left: 520px; top: 250px;
    display: flex; align-items: center; gap: 14px;
  }
  .brand-dot {
    width: 14px; height: 14px; border-radius: 50%;
    background: var(--brand-green);
  }
  .brand-name {
    font-family: "Marcellus", serif;
    font-size: 46px; color: var(--brand-green); line-height: 1;
  }
</style>
</head>
<body>
  <div class="card">
    <svg class="card-bg" width="1000" height="568" viewBox="0 0 1000 568">
      <defs>
        <linearGradient id="leftPanel" x1="0" y1="0" x2="1" y2="1">
          <stop offset="0" stop-color="#2d4f1d"/>
          <stop offset="0.45" stop-color="var(--green-mid)"/>
          <stop offset="1" stop-color="var(--green-soft)"/>
        </linearGradient>
        <radialGradient id="frostPanel" cx="0.55" cy="0.45" r="0.6">
          <stop offset="0" stop-color="#efece6"/>
          <stop offset="1" stop-color="var(--frost-edge)"/>
        </radialGradient>
      </defs>
      <rect width="1000" height="568" fill="url(#leftPanel)"/>
      <rect x="560" width="440" height="568" fill="url(#frostPanel)"/>
      <circle cx="716" cy="283" r="267" fill="url(#frostPanel)"/>
      <circle cx="716" cy="283" r="267" fill="none" stroke="var(--green-deep)" stroke-width="4"/>
    </svg>

    <div class="contact">
      <div class="contact-name">Daniel Reyes</div>
      <div class="contact-title">President</div>
      <div class="contact-address">4120 Willow Crest Road<br>Fairview, Alaska 40218</div>
      <ul class="contact-lines">
        <li><svg viewBox="0 0 24 24"><path d="M6.6 10.8a15 15 0 0 0 6.6 6.6l2.2-2.2a1 1 0 0 1 1-.25 11.4 11.4 0 0 0 3.6.57 1 1 0 0 1 1 1V20a1 1 0 0 1-1 1A17 17 0 0 1 3 4a1 1 0 0 1 1-1h3.5a1 1 0 0 1 1 1c0 1.25.2 2.45.57 3.57a1 1 0 0 1-.25 1z"/></svg>555-204-7316</li>
        <li><svg viewBox="0 0 24 24"><path d="M7 1h10a2 2 0 0 1 2 2v18a2 2 0 0 1-2 2H7a2 2 0 0 1-2-2V3a2 2 0 0 1 2-2zm0 3v14h10V4zm5 15.5a1 1 0 1 0 0 2 1 1 0 0 0 0-2z"/></svg>555-318-6042</li>
        <li><svg viewBox="0 0 24 24"><path d="M2 6h20v12H2zm2 2v.4l8 5 8-5V8l-8 5z"/></svg>hello@pineharbor.com</li>
        <li><svg viewBox="0 0 24 24"><path d="M12 2a10 10 0 1 0 0 20 10 10 0 0 0 0-20zm0 2c1 1.3 1.8 3.1 2.1 5H9.9C10.2 7.1 11 5.3 12 4zM4.3 11h3.6c.1 1.8.5 3.5 1.2 4.9A8 8 0 0 1 4.3 11zm5.6 0h4.2a12 12 0 0 1-2.1 6 12 12 0 0 1-2.1-6zm6.2 0h3.6a8 8 0 0 1-4.8 4.9c.7-1.4 1.1-3.1 1.2-4.9z"/></svg>www.pineharbor.com</li>
      </ul>
    </div>

    <div class="brand">
      <span class="brand-dot"></span>
      <span class="brand-name">PineHarbor</span>
    </div>
  </div>
</body>
</html>
```